Website re-design wedding music business

I need my wordpress wedding music website redesigned. I'm a wedding pianist and also provide duo/trio entertainment with other musicians and looking for an overhaul of my wordpress site.

Website: tollykessing.com.au

Target Market(s)

brides; engaged couples

Industry/Entity Type

Wedding

Number of Pages Required

5+ page

Colors

Designer to choose colors to be used in the design.

Requirements
Must have
• I'm looking to overhaul my website which is looking rather tired after 4 years. It is functional but not inviting to visitors. Initially my website started out as a solo piano player providing music for wedding. It is gradually growing now where brides can book
• 1) Solo Piano
• 2) Duo (any combination of Piano / Cello / Vocalist / Violin)
• 3) Trio (any combination of Piano/ Cello /Vocalist / Violin)
• in future it may increase to 4 / 5 /6 piece bands so that needs to be taken into account for the future growth where I'll recruit other musicians.
• Some other functionality I'd like to see
• - Visitors want a calendar to know availability of musicians
• - Automatically providing enquiry price & discount (if applicable)
• - Automating the booking form process (manual) - There's a PDF form I send to the customer after we go back/forth on email on songs/price etc but if more of it could be automated online that would be great. If move to online it would be good to be able to override the set prices with a custom price and also providing a payment gateway
• More Flexibility on pricing - customer selects type of artists they want and it calculates a price based on who they have chosen whether it is a ceremony or canapes or reception (or combination of any). Extra transport fee is added if >50km out of Melbourne.
• How would you re-design this website. Imagine you are a bride/groom looking to book wedding music services. I would love to see some concepts .
• Please indicate any other fees required for your submission and level of support post this competition. I would like this to be an on-going relationship.
Nice to have
• I'd preferably like the website to be in wordpress as I've been familiar with it over time and can do basic updates in the back end. Happy for other suggestions if you can convince me I should move away from wordpress.

```html
<!DOCTYPE html>
<html lang="en">
<head>
<meta charset="utf-8">
<title>Tolly Kessing – Wedding Pianist</title>
<link href="https://fonts.googleapis.com/css2?family=Roboto:wght@300;400;500;700;900&display=swap" rel="stylesheet">
<style>
:root{
  --ink:#111111;
  --black:#0b0b0b;
  --white:#ffffff;
  --paper:#f6f6f6;
  --grey:#8a8a8a;
  --muted:#555555;
  --line:#cfcfcf;
  --gold:#c8a45c;
  --gold-soft:#e3cf9e;
}
*{box-sizing:border-box;margin:0;padding:0}
html,body{width:1200px;height:3468px;overflow:hidden;background:var(--white)}
body{font-family:'Roboto',Arial,sans-serif;color:var(--ink)}
.page{position:relative;width:1200px;height:3468px;overflow:hidden}
section,header,footer{position:absolute;left:0;width:1200px}
.abs{position:absolute}
.btn{position:absolute;display:flex;align-items:center;justify-content:center;border-radius:20px;font-size:12px;font-weight:500}
.btn-dark{background:var(--ink);color:var(--white)}
.btn-light{background:var(--white);color:var(--ink)}

/* header + hero */
.site-header{top:0;height:527px;background:linear-gradient(180deg,#fbfbfb,#f1f1f1)}
.brand{left:254px;top:20px;display:flex;align-items:center;gap:8px;font-size:15px;font-weight:700;letter-spacing:.5px}
.brand-dot{width:44px;height:44px;border-radius:50%;background:var(--ink)}
.contact-strip{top:36px;font-size:11.5px;color:var(--muted);white-space:nowrap}
.contact-strip b{color:var(--ink);font-weight:700}
.main-nav{left:252px;top:84px;display:flex;gap:14px;font-size:11.5px;color:var(--grey);white-space:nowrap}
.main-nav .active{color:var(--ink);font-weight:700}
.search-icon{left:936px;top:81px}
.hero-stage{left:260px;top:140px;width:680px;height:380px;background:radial-gradient(ellipse at 50% 60%,#ffffff 30%,rgba(255,255,255,0) 70%)}
.hero-pianist{left:300px;top:220px;width:300px;height:300px;border-radius:40% 40% 6px 6px;background:linear-gradient(160deg,#2a2a32 0%,#1d1d24 45%,#f4f4f4 46%,#e3e3e3 100%)}
.hero-cellist{left:660px;top:150px;width:210px;height:370px;border-radius:45% 45% 6px 6px;background:linear-gradient(180deg,#d9b48f 0%,#2c4f9a 22%,#1a1a1a 55%,#7a3a1c 75%,#5a2a14 100%)}
.hero-shadow{left:320px;top:512px;width:560px;height:18px;border-radius:50%;background:radial-gradient(ellipse,rgba(0,0,0,.25),transparent 70%)}

/* about */
.about{top:527px;height:525px;background:var(--paper)}
.about h2{position:absolute;left:134px;top:70px;font-size:40px;font-weight:900}
.about p{position:absolute;left:134px;top:138px;width:410px;font-size:14.5px;line-height:20px;color:var(--muted)}
.about ul{position:absolute;left:134px;top:220px;list-style:none;font-size:14px;color:var(--muted)}
.about li{height:29px}
.about li::before{content:"»";margin-right:8px;color:var(--ink)}
.about .btn{left:134px;top:375px;width:146px;height:39px}
.award-frame{left:600px;top:46px;width:396px;height:396px;border-radius:50%;background:radial-gradient(circle,transparent 58%,var(--gold-soft) 60%,var(--gold) 72%,transparent 74%)}
.award-photo{left:658px;top:104px;width:280px;height:280px;border-radius:50%;background:radial-gradient(circle at 50% 35%,#6a5a48 0%,#2a2622 45%,#0e0e0e 80%)}
.about-curve{left:0;top:420px}

/* events */
.events{top:1052px;height:566px;background:radial-gradient(ellipse at 50% 30%,#2a2a2a,#050505 70%)}
.section-title{position:absolute;left:0;width:100%;text-align:center;font-weight:900}
.events .section-title{top:68px;font-size:42px;color:var(--white)}
.events .sub{position:absolute;top:122px;width:100%;text-align:center;font-size:13px;color:#bdbdbd}
.event-card{position:absolute;top:166px;width:197px;height:239px;color:var(--white);overflow:hidden}
.event-card .bg{position:absolute;inset:0}
.event-card .label{position:absolute;left:10px;top:10px;font-size:11px}
.event-card .date{position:absolute;left:10px;top:28px;font-size:28px;font-weight:700}
.event-card .time{position:absolute;left:10px;top:162px;font-size:13px;font-weight:700}
.event-card .desc{position:absolute;left:10px;top:180px;width:180px;font-size:9.5px;line-height:11px;color:#e5e5e5}
.add-cal{position:absolute;top:414px;display:flex;align-items:center;gap:8px;font-size:11px;color:var(--white)}
.add-cal i{width:20px;height:20px;border-radius:50%;background:var(--white);color:var(--ink);font-style:normal;display:flex;align-items:center;justify-content:center;font-weight:700}
.slide-arrow{position:absolute;width:24px;height:24px;display:flex;align-items:center;justify-content:center;border-radius:3px}
.events .btn{left:528px;top:493px;width:144px;height:40px}

/* music */
.music{top:1618px;height:393px;background:linear-gradient(180deg,#efefef,#e3e3e3)}
.player{position:absolute;left:250px;width:393px;height:50px;background:var(--white);box-shadow:0 2px 6px rgba(0,0,0,.2);display:flex;align-items:center;padding:0 12px;gap:10px}
.player .ctrl{display:flex;align-items:center;gap:6px}
.player .track{flex:1;position:relative;height:100%}
.player .name{position:absolute;left:0;top:10px;font-size:10px;font-weight:700}
.player .bar{position:absolute;left:0;right:42px;top:30px;height:2px;background:var(--line)}
.player .bar span{display:block;width:38%;height:2px;background:var(--ink)}
.player .time{position:absolute;right:0;top:25px;font-size:9px;color:var(--muted)}
.music h2{position:absolute;left:698px;top:56px;font-size:42px;font-weight:900}
.music p{position:absolute;left:666px;top:152px;width:282px;font-size:13px;line-height:19px;color:var(--muted);text-align:justify}
.music .btn{left:735px;top:273px;width:144px;height:42px}

/* availability */
.availability{top:2011px;height:352px;background:var(--black)}
.availability h2{position:absolute;left:0;width:580px;top:52px;text-align:center;color:var(--white);font-size:44px;line-height:48px;font-weight:900}
.availability h2 span{font-weight:400}
.date-field{position:absolute;top:176px;height:35px;border:1px solid #777;color:#ddd;font-size:11px;display:flex;align-items:center;justify-content:space-between;padding:0 12px}
.availability .check{position:absolute;left:238px;top:243px;width:120px;height:35px;background:var(--white);color:var(--ink);font-size:11px;font-weight:500;display:flex;align-items:center;justify-content:center}
.pianist-photo{left:600px;top:0;width:600px;height:352px;background:radial-gradient(ellipse at 65% 55%,#1b1d24 0%,#1b1d24 28%,rgba(27,29,36,0) 45%),linear-gradient(180deg,#4a5230 0%,#8f9a62 40%,#b7bd8c 55%,#6c7a44 75%,#3a3f2a 100%)}

/* testimonials */
.testimonials{top:2363px;height:388px;background:var(--white)}
.testimonials .section-title{top:40px;font-size:34px}
.avatar{left:540px;top:100px;width:120px;height:120px;border-radius:50%;border:4px solid var(--white);box-shadow:0 0 0 2px var(--ink);background:radial-gradient(circle at 50% 35%,#c9a78a 0%,#b58f72 22%,#e6e6e6 24%,#cfd3da 50%,#2d3340 70%)}
.quote{position:absolute;left:306px;top:238px;width:588px;text-align:center;font-size:12.5px;line-height:17px;color:var(--muted);font-style:italic}
.author{position:absolute;top:300px;width:100%;text-align:center;font-size:15px;font-weight:700}
.role{position:absolute;top:321px;width:100%;text-align:center;font-size:9px;color:var(--grey)}
.dots{position:absolute;top:340px;left:0;width:100%;display:flex;justify-content:center;gap:8px}
.dots i{width:7px;height:7px;border-radius:50%;border:1px solid var(--ink)}
.dots i.on{background:var(--ink)}

/* gallery */
.gallery{top:2751px;height:266px;display:flex}
.gallery .shot{height:266px;flex:1}
.gal-arrow{position:absolute;top:113px;width:42px;height:42px;border-radius:50%;border:2px solid var(--white);background:rgba(0,0,0,.35);display:flex;align-items:center;justify-content:center}

/* contact */
.contact{top:3017px;height:405px;background:linear-gradient(180deg,#1e1e1e,#111)}
.contact h2{position:absolute;left:113px;top:48px;font-size:34px;font-weight:900;color:var(--white)}
.contact .sub{position:absolute;left:113px;top:90px;font-size:14px;color:#bdbdbd}
.field{position:absolute;height:28px;border:1px solid #9a9a9a;color:#cfcfcf;font-size:10px;padding:7px 8px}
.send{position:absolute;left:113px;top:317px;width:141px;height:34px;background:var(--white);font-size:12px;font-weight:700;display:flex;align-items:center;justify-content:center}
.location h3{position:absolute;left:805px;top:48px;font-size:36px;font-weight:900;color:var(--white)}
.location p{position:absolute;left:808px;top:100px;width:270px;font-size:12.5px;line-height:17px;color:#cfcfcf}
.loc-row{position:absolute;left:808px;display:flex;align-items:center;gap:12px;font-size:12px;color:#e0e0e0}
.location h4{position:absolute;left:812px;top:216px;font-size:21px;font-weight:900;color:var(--white)}
.location .follow{position:absolute;left:812px;top:244px;font-size:11px;color:#cfcfcf}
.socials{position:absolute;left:811px;top:276px;display:flex;gap:13px}
.socials i{width:40px;height:40px;border-radius:50%;background:var(--white);display:flex;align-items:center;justify-content:center}
.socials i::after{content:"";width:30px;height:30px;border-radius:50%;border:2px solid var(--ink)}

/* footer */
.site-footer{top:3422px;height:46px;background:var(--black);color:#bdbdbd;font-size:10px;display:flex;align-items:center;padding-left:113px}
.site-footer b{color:var(--white);margin:0 4px}
</style>
</head>
<body>
<div class="page">

<header class="site-header">
  <div class="abs brand"><span class="brand-dot"></span>TOLLY KESSING</div>
  <div class="abs contact-strip" style="left:575px"><b>Email</b> : hello@tollykessing.com.au</div>
  <div class="abs contact-strip" style="left:798px"><b>Phone Number</b> : 0400 555 218</div>
  <nav class="abs main-nav">
    <span class="active">Home</span><span>About Tolly</span><span>Events</span><span>Music</span><span>Video</span><span>Repertoire</span><span>Prices</span><span>Gallery</span><span>Testimonials</span><span>Buy CD</span><span>FAQs</span><span>Contact</span>
  </nav>
  <svg class="abs search-icon" width="14" height="14" viewBox="0 0 14 14"><circle cx="6" cy="6" r="4.5" fill="none" stroke="#111" stroke-width="1.6"/><line x1="9.3" y1="9.3" x2="13" y2="13" stroke="#111" stroke-width="1.6"/></svg>
  <div class="abs hero-stage"></div>
  <div class="abs hero-shadow"></div>
  <div class="abs hero-pianist" role="img" aria-label="Pianist in a dark suit at a white grand piano"></div>
  <div class="abs hero-cellist" role="img" aria-label="Cellist in a blue and black dress holding her cello"></div>
</header>

<section class="about">
  <h2>ABOUT TOLLY</h2>
  <p>Tolly Kessing is a Melbourne professional pianist with over 5 years experience within the wedding industry and has played piano for more than 30 years.</p>
  <ul>
    <li>Wedding Ceremony, Canapés &amp; Receptions</li>
    <li>Corporate events</li>
    <li>Anniversaries (e.g. birthdays)</li>
    <li>Special Events</li>
    <li>Accompanist for singers.</li>
  </ul>
  <div class="btn btn-dark">Read More</div>
  <div class="abs award-frame" role="img" aria-label="Gold ornamental frame"></div>
  <div class="abs award-photo" role="img" aria-label="Pianist holding a music industry award"></div>
  <svg class="abs about-curve" width="1200" height="105" viewBox="0 0 1200 105"><path d="M0 40 Q600 110 1200 40 L1200 105 L0 105 Z" fill="#0b0b0b"/><path d="M0 40 Q600 110 1200 40" fill="none" stroke="#ffffff" stroke-width="6"/></svg>
</section>

<section class="events">
  <h2 class="section-title">UPCOMING EVENTS</h2>
  <div class="sub">Lorem Ipsum is simply dummy text of the printing and typesetting industry.</div>

  <div class="event-card" style="left:88px"><div class="bg" role="img" aria-label="Piano keys at an event" style="background:linear-gradient(180deg,#3a2a20 0%,#6a4a34 45%,#d8d0c4 62%,#1a1410 75%,#111 100%)"></div><div class="label">Private event – Aspendale (tbc)</div><div class="date">July, 30</div><div class="time">2:00 pm – 3:00 pm</div><div class="desc">Soft piano sets through the ceremony, signing and photos, with requests taken ahead of the day for the couple.</div></div>
  <div class="event-card" style="left:294px"><div class="bg" role="img" aria-label="Musicians performing at a wedding" style="background:linear-gradient(180deg,#5a3322 0%,#2a1e1a 40%,#7a5a44 60%,#1a1410 80%,#111 100%)"></div><div class="label">Wedding Ceremony &amp; Canapés</div><div class="date">Aug.10</div><div class="time">3:30 pm – 6:00 pm</div><div class="desc">Soft piano sets through the ceremony, signing and photos, with requests taken ahead of the day for the couple.</div></div>
  <div class="event-card" style="left:500px"><div class="bg" role="img" aria-label="Pianist at a corporate event" style="background:linear-gradient(180deg,#4a3a2c 0%,#2a2420 40%,#8a6a4c 60%,#1a1410 80%,#111 100%)"></div><div class="label">Corporate event Grandview Hotel</div><div class="date">Sep,25</div><div class="time">7:30 pm – 9:30 pm</div><div class="desc">Soft piano sets through the ceremony, signing and photos, with requests taken ahead of the day for the couple.</div></div>
  <div class="event-card" style="left:706px"><div class="bg" role="img" aria-label="Pianist at a wedding ceremony" style="background:linear-gradient(180deg,#3a2e26 0%,#4a3a2e 40%,#6e5a48 60%,#1a1410 80%,#111 100%)"></div><div class="label">wedding ceremony</div><div class="date">Oct, 15</div><div class="time">8:00 am – 5:00 pm</div><div class="desc">Soft piano sets through the ceremony, signing and photos, with requests taken ahead of the day for the couple.</div></div>
  <div class="event-card" style="left:912px"><div class="bg" role="img" aria-label="Pianist at a wedding reception" style="background:linear-gradient(180deg,#2e2a2a 0%,#5a4a40 40%,#9a8270 60%,#1a1410 80%,#111 100%)"></div><div class="label">Wedding reception Lakeside Lodge</div><div class="date">Nov, 09</div><div class="time">8:00 am – 10:00 pm</div><div class="desc">Soft piano sets through the ceremony, signing and photos, with requests taken ahead of the day for the couple.</div></div>

  <div class="add-cal" style="left:88px"><i>+</i>Add to Calendar</div>
  <div class="add-cal" style="left:294px"><i>+</i>Add to Calendar</div>
  <div class="add-cal" style="left:500px"><i>+</i>Add to Calendar</div>
  <div class="add-cal" style="left:706px"><i>+</i>Add to Calendar</div>
  <div class="add-cal" style="left:912px"><i>+</i>Add to Calendar</div>

  <div class="slide-arrow" style="left:90px;top:500px;background:#2d3a4a"><svg width="10" height="10" viewBox="0 0 10 10"><path d="M7 1 L3 5 L7 9" fill="none" stroke="#fff" stroke-width="2"/></svg></div>
  <div class="slide-arrow" style="left:1086px;top:500px;background:#fff"><svg width="10" height="10" viewBox="0 0 10 10"><path d="M3 1 L7 5 L3 9" fill="none" stroke="#111" stroke-width="2"/></svg></div>
  <div class="btn btn-light">See All Events</div>
</section>

<section class="music">
  <div class="player" style="top:62px"><div class="ctrl"><svg width="14" height="10"><path d="M7 0 L0 5 L7 10Z M14 0 L7 5 L14 10Z" fill="#111"/></svg><svg width="30" height="30" viewBox="0 0 30 30"><circle cx="15" cy="15" r="15" fill="#111"/><rect x="11" y="10" width="3" height="10" fill="#fff"/><rect x="16" y="10" width="3" height="10" fill="#fff"/></svg><svg width="14" height="10"><path d="M0 0 L7 5 L0 10Z M7 0 L14 5 L7 10Z" fill="#111"/></svg></div><div class="track"><div class="name">MORNING LIGHT - SOLO</div><div class="bar"><span></span></div><div class="time">03:28</div></div></div>
  <div class="player" style="top:134px"><div class="ctrl"><svg width="14" height="10"><path d="M7 0 L0 5 L7 10Z M14 0 L7 5 L14 10Z" fill="#111"/></svg><svg width="30" height="30" viewBox="0 0 30 30"><circle cx="15" cy="15" r="15" fill="#111"/><path d="M12 9 L21 15 L12 21Z" fill="#fff"/></svg><svg width="14" height="10"><path d="M0 0 L7 5 L0 10Z M7 0 L14 5 L7 10Z" fill="#111"/></svg></div><div class="track"><div class="name">MORNING LIGHT - SOLO</div><div class="bar"><span style="width:0"></span></div><div class="time">03:28</div></div></div>
  <div class="player" style="top:208px"><div class="ctrl"><svg width="14" height="10"><path d="M7 0 L0 5 L7 10Z M14 0 L7 5 L14 10Z" fill="#111"/></svg><svg width="30" height="30" viewBox="0 0 30 30"><circle cx="15" cy="15" r="15" fill="#111"/><path d="M12 9 L21 15 L12 21Z" fill="#fff"/></svg><svg width="14" height="10"><path d="M0 0 L7 5 L0 10Z M7 0 L14 5 L7 10Z" fill="#111"/></svg></div><div class="track"><div class="name">MORNING LIGHT - SOLO</div><div class="bar"><span style="width:0"></span></div><div class="time">03:28</div></div></div>
  <div class="player" style="top:278px"><div class="ctrl"><svg width="14" height="10"><path d="M7 0 L0 5 L7 10Z M14 0 L7 5 L14 10Z" fill="#111"/></svg><svg width="30" height="30" viewBox="0 0 30 30"><circle cx="15" cy="15" r="15" fill="#111"/><path d="M12 9 L21 15 L12 21Z" fill="#fff"/></svg><svg width="14" height="10"><path d="M0 0 L7 5 L0 10Z M7 0 L14 5 L7 10Z" fill="#111"/></svg></div><div class="track"><div class="name">MORNING LIGHT - SOLO</div><div class="bar"><span style="width:0"></span></div><div class="time">03:28</div></div></div>

  <h2>THE MUSIC</h2>
  <svg class="abs" style="left:767px;top:112px" width="80" height="16" viewBox="0 0 80 16"><g stroke="#b9a0a0" stroke-width="1.5"><line x1="4" y1="8" x2="4" y2="8.5"/><line x1="10" y1="6" x2="10" y2="10"/><line x1="16" y1="4" x2="16" y2="12"/><line x1="22" y1="7" x2="22" y2="9"/><line x1="28" y1="2" x2="28" y2="14"/><line x1="34" y1="5" x2="34" y2="11"/><line x1="40" y1="1" x2="40" y2="15"/><line x1="46" y1="5" x2="46" y2="11"/><line x1="52" y1="3" x2="52" y2="13"/><line x1="58" y1="6" x2="58" y2="10"/><line x1="64" y1="4" x2="64" y2="12"/><line x1="70" y1="7" x2="70" y2="9"/><line x1="76" y1="8" x2="76" y2="8.5"/></g></svg>
  <p>Tolly's easy-listening, "cocktail" piano style comprises a varied repertoire of popular, movie and show tunes and includes artists below alongside many others. Tolly also has an extensive repertoire of classical music for weddings.</p>
  <div class="btn btn-dark">See All Music</div>
</section>

<section class="availability">
  <h2>AVAILABILITY OF<br><span>MUSICIANS</span></h2>
  <div class="date-field" style="left:88px;width:194px">From<svg width="12" height="12"><g fill="#ddd"><rect x="0" y="0" width="3" height="3"/><rect x="4.5" y="0" width="3" height="3"/><rect x="9" y="0" width="3" height="3"/><rect x="0" y="4.5" width="3" height="3"/><rect x="4.5" y="4.5" width="3" height="3"/><rect x="9" y="4.5" width="3" height="3"/><rect x="0" y="9" width="3" height="3"/><rect x="4.5" y="9" width="3" height="3"/><rect x="9" y="9" width="3" height="3"/></g></svg></div>
  <div class="date-field" style="left:302px;width:196px">To<svg width="12" height="12"><g fill="#ddd"><rect x="0" y="0" width="3" height="3"/><rect x="4.5" y="0" width="3" height="3"/><rect x="9" y="0" width="3" height="3"/><rect x="0" y="4.5" width="3" height="3"/><rect x="4.5" y="4.5" width="3" height="3"/><rect x="9" y="4.5" width="3" height="3"/><rect x="0" y="9" width="3" height="3"/><rect x="4.5" y="9" width="3" height="3"/><rect x="9" y="9" width="3" height="3"/></g></svg></div>
  <div class="check">Check Availability</div>
  <div class="abs pianist-photo" role="img" aria-label="Pianist in a suit playing outdoors in a park"></div>
</section>

<section class="testimonials">
  <h2 class="section-title">TESTIMONIALS</h2>
  <div class="abs avatar" role="img" aria-label="Client portrait"></div>
  <p class="quote">"Lorem ipsum dolor sit amet, consectetur adipiscing elit, sed do eiusmod tempor incididunt ut labore et dolore magna aliqua. Ut enim ad minim veniam, quis nostrud exercitation ullamco laboris nisi ut aliquip ex ea commodo consequat.</p>
  <div class="author">JOHN DOE</div>
  <div class="role">CREATIVE HEADS INC.</div>
  <div class="dots"><i class="on"></i><i></i><i></i><i></i></div>
</section>

<section class="gallery">
  <div class="shot" role="img" aria-label="Hands playing piano keys" style="background:linear-gradient(180deg,#2a1c14 0%,#8a6048 40%,#d9b89a 60%,#eae4da 78%,#1a1a1a 100%)"></div>
  <div class="shot" role="img" aria-label="Pianist at a white grand piano outdoors" style="background:linear-gradient(180deg,#3a4a2a 0%,#5a6a3e 35%,#1c1c22 55%,#e8e8e4 75%,#b8b4a8 100%)"></div>
  <div class="shot" role="img" aria-label="Cellist performing" style="background:linear-gradient(180deg,#3a3a32 0%,#2a3f7a 30%,#151515 55%,#9a4a22 75%,#cfc8bc 100%)"></div>
  <div class="shot" role="img" aria-label="Trio of musicians in a church" style="background:linear-gradient(180deg,#6a2e18 0%,#3a1f12 30%,#1a1a1e 60%,#e4e0d8 82%,#5a2a18 100%)"></div>
  <div class="shot" role="img" aria-label="Close view of piano keys" style="background:linear-gradient(160deg,#1a120c 0%,#5a3a24 35%,#e8dcc4 55%,#1a1410 70%,#c7b08a 100%)"></div>
  <div class="gal-arrow" style="left:16px"><svg width="12" height="12" viewBox="0 0 12 12"><path d="M8 1 L3 6 L8 11" fill="none" stroke="#fff" stroke-width="2"/></svg></div>
  <div class="gal-arrow" style="left:1132px"><svg width="12" height="12" viewBox="0 0 12 12"><path d="M4 1 L9 6 L4 11" fill="none" stroke="#fff" stroke-width="2"/></svg></div>
</section>

<section class="contact">
  <h2>CONTACT TOLLY KESSING</h2>
  <div class="sub">Lorem Ipsum is simply dummy text of the printing and typesetting industry.</div>
  <div class="field" style="left:113px;top:127px;width:157px">Your Name</div>
  <div class="field" style="left:284px;top:127px;width:157px">Your Email</div>
  <div class="field" style="left:455px;top:127px;width:157px">Your Phone</div>
  <div class="field" style="left:113px;top:169px;width:499px;height:136px">Your Message</div>
  <div class="send">SEND</div>

  <div class="location">
    <h3>LOCATION</h3>
    <p>Have Tolly Kessing play at your function. Get in touch below or give Tolly a call on</p>
    <div class="loc-row" style="top:150px"><svg width="14" height="11" viewBox="0 0 14 11"><rect x="0.5" y="0.5" width="13" height="10" fill="none" stroke="#fff"/><path d="M0.5 0.5 L7 6 L13.5 0.5" fill="none" stroke="#fff"/></svg>hello@tollykessing.com.au</div>
    <div class="loc-row" style="top:173px"><svg width="14" height="14" viewBox="0 0 14 14"><rect x="3.5" y="0.5" width="7" height="13" rx="1" fill="none" stroke="#fff"/></svg>Phone 0400 555 218</div>
    <h4>JOIN US ON</h4>
    <div class="follow">Follow us</div>
    <div class="socials" aria-label="Social links"><i></i><i></i><i></i><i></i><i></i></div>
  </div>
</section>

<footer class="site-footer">Copyright © 2017 <b>Tolly Kessing.</b> All Rights Reserved.</footer>

</div>
</body>
</html>
```